"Harrow Crest Builders" is a residential building company and needs a new business card design and may re

We would like a redesign based on the existing logo, and would like to see a new font as well. We are bespoke home builders who build sustainable energy efficient homes.

Industry/Entity Type

Construction

Contact Information for Business Card

Business card size 40mm x 90mm

Colors

Designer to choose colors to be used in the design.

```html
<!DOCTYPE html>
<html lang="en">
<head>
<meta charset="utf-8">
<title>Harrow Crest Builders – Business Card</title>
<link rel="stylesheet" href="https://fonts.googleapis.com/css2?family=Montserrat:wght@300;400;600&family=Open+Sans:wght@400;600&display=swap">
<style>
  :root {
    --stage: #3b3b3b;
    --card-light: #ffffff;
    --card-dark: #262626;
    --ink: #4a4a4a;
    --ink-strong: #333333;
    --muted: #d9d9d9;
    --accent: #8dc63f;
  }
  * { box-sizing: border-box; margin: 0; padding: 0; }
  html, body {
    width: 1058px; height: 1200px; overflow: hidden;
    background: var(--stage);
  }
  .canvas {
    position: relative; width: 1058px; height: 1200px;
    font-family: "Open Sans", Arial, sans-serif;
  }
  .wordmark {
    display: flex; align-items: center; gap: 14px;
    font-family: "Montserrat", Arial, sans-serif;
    font-weight: 400; white-space: nowrap;
  }
  .wordmark__square { display: inline-block; flex: none; }
  .brand-header {
    position: absolute; left: 60px; top: 70px;
    font-size: 42px; color: var(--muted);
  }
  .brand-header .wordmark__square { width: 46px; height: 46px; background: var(--accent); }

  .card {
    position: absolute; left: 149px; width: 760px; height: 338px;
    box-shadow: 0 10px 24px rgba(0,0,0,.45);
  }
  .card--front { top: 210px; background: var(--card-light); }
  .card--back  { top: 640px; background: var(--card-dark); }

  .card--front .wordmark {
    position: absolute; right: 40px; top: 40px;
    font-size: 26px; color: var(--ink); gap: 10px;
  }
  .card--front .wordmark__square { width: 26px; height: 26px; background: var(--accent); }

  .contact-person { position: absolute; left: 40px; top: 118px; color: var(--ink); }
  .contact-person__name { font-family: "Montserrat", Arial, sans-serif; font-weight: 300; font-size: 26px; }
  .contact-person__name strong { font-weight: 600; color: var(--ink-strong); }
  .contact-person__phone { font-size: 22px; margin-top: 4px; }

  .contact-list { position: absolute; left: 40px; top: 212px; list-style: none; }
  .contact-list li {
    display: flex; align-items: center; gap: 12px;
    font-size: 16px; color: var(--ink); height: 25px;
  }
  .contact-list svg { width: 18px; height: 18px; flex: none; }
  .registration { position: absolute; left: 40px; top: 293px; font-size: 16px; color: var(--accent); }

  .card--back .wordmark {
    position: absolute; left: 50%; top: 50%; transform: translate(-50%, -50%);
    font-size: 38px; color: var(--muted);
  }
  .card--back .wordmark__square { width: 40px; height: 40px; background: var(--accent); }
</style>
</head>
<body>
<main class="canvas">
  <header class="brand-header wordmark">
    <span class="wordmark__square"></span>Harrow Crest Builders
  </header>

  <section class="card card--front" aria-label="Business card front">
    <div class="wordmark"><span class="wordmark__square"></span>Harrow Crest Builders</div>
    <div class="contact-person">
      <p class="contact-person__name">Daniel <strong>Marrow</strong></p>
      <p class="contact-person__phone">0400 555 018</p>
    </div>
    <ul class="contact-list">
      <li>
        <svg viewBox="0 0 18 18" aria-hidden="true"><rect x="1" y="4" width="16" height="11" rx="1" fill="var(--accent)"/><path d="M1 5l8 6 8-6" fill="none" stroke="#fff" stroke-width="1.4"/></svg>
        daniel@harrowcrestbuilders.com.au
      </li>
      <li>
        <svg viewBox="0 0 18 18" aria-hidden="true" fill="none" stroke="var(--accent)" stroke-width="1.4"><circle cx="9" cy="9" r="7.5"/><ellipse cx="9" cy="9" rx="3.3" ry="7.5"/><path d="M1.5 9h15M3 5h12M3 13h12"/></svg>
        www.harrowcrestbuilders.com.au
      </li>
      <li>
        <svg viewBox="0 0 18 18" aria-hidden="true"><path d="M9 1a6 6 0 0 0-6 6c0 4.5 6 10 6 10s6-5.5 6-10a6 6 0 0 0-6-6z" fill="var(--accent)"/><circle cx="9" cy="7" r="2.2" fill="#fff"/></svg>
        PO Box 1180 Hillcrest LPO Northvale WA 6999
      </li>
    </ul>
    <p class="registration">Registration 40318 ABN: 12 345 678 901</p>
  </section>

  <section class="card card--back" aria-label="Business card back">
    <div class="wordmark"><span class="wordmark__square"></span>Harrow Crest Builders</div>
  </section>
</main>
</body>
</html>
```